Cedarline Joinery eye catching business card

I need an eye catching business card that reflects my traditional, fun, handmade woodcraft shop. I make high end custom furniture and fine woodworking products, a lot of which are rustic, natural looking. We are a small shop but we produce awesome, one of a kind wood products, and our business card should reflect that. Our target audience is young professionals to retired folks who want a quality, local, handmade product. I'd like the Shop Nearby logo somewhere on the card, BUT not overwhelming, the main focus is my Logo, no preference on color whichever looks the best. Visit my website to get a feel for my company. Cedarlinejoinery.com
Target Market(s)
young professionals to retired folks. Any one who wants to furnish their home with quality handcrafted products.
Industry/Entity Type
Business
Contact Information for Business Card
Marlo Finch (555)417-6382
marlo@cedarlinejoinery.com
www.cedarlinejoinery.com
Look and feel

```html
<!DOCTYPE html>
<html lang="en">
<head>
<meta charset="utf-8">
<title>Cedarline Joinery — Business Card</title>
<link rel="stylesheet" href="https://fonts.googleapis.com/css2?family=Oswald:wght@400;500;600&family=Montserrat:wght@500&display=swap">
<style>
  :root {
    --stage: #1c1c1d;
    --card-black: #111213;
    --card-black-edge: #1d1f21;
    --ink-light: #d9d6d0;
    --ink-soft: #c4c1bb;
    --wood-dark: #4a2a12;
    --wood-mid: #8a5a2e;
    --wood-light: #b07a43;
    --wood-ink: #2e1808;
  }
  * { box-sizing: border-box; margin: 0; padding: 0; }
  html, body {
    width: 1200px; height: 871px; overflow: hidden;
    background: var(--stage);
  }
  .stage {
    position: relative; width: 1200px; height: 871px;
    display: flex; flex-direction: column; align-items: center; justify-content: center;
    gap: 40px;
  }
  .card {
    position: relative; width: 630px; height: 360px;
    border-radius: 4px; overflow: hidden;
    box-shadow: 0 18px 40px rgba(0,0,0,.6);
  }

  /* Back side: wood */
  .card-back .wood {
    position: absolute; inset: 0;
    background:
      linear-gradient(90deg, rgba(0,0,0,.12) 0 1px, transparent 1px) 0 0 / 42px 100%,
      radial-gradient(ellipse at 45% 35%, var(--wood-light) 0%, var(--wood-mid) 45%, var(--wood-dark) 100%);
  }
  .back-brand {
    position: absolute; left: 0; right: 0; top: 92px; text-align: center;
    font-family: "Oswald", sans-serif; font-weight: 600;
    color: var(--wood-ink); text-transform: uppercase;
    font-size: 62px; letter-spacing: 6px; line-height: 1.05;
  }
  .back-url {
    position: absolute; left: 0; right: 0; bottom: 40px; text-align: center;
    font-family: "Oswald", sans-serif; font-weight: 600;
    color: var(--wood-ink); text-transform: uppercase;
    font-size: 26px; letter-spacing: 4px;
  }

  /* Front side: black */
  .card-front {
    background: radial-gradient(ellipse at 50% 30%, var(--card-black-edge), var(--card-black) 75%);
  }
  .front-brand {
    position: absolute; left: 40px; top: 100px; width: 250px;
  }
  .brand-name {
    font-family: "Oswald", sans-serif; font-weight: 600;
    color: var(--ink-light); text-transform: uppercase;
    font-size: 38px; letter-spacing: 4px; line-height: 1.1;
  }
  .tagline {
    margin-top: 18px;
    font-family: "Montserrat", sans-serif; font-weight: 500;
    color: var(--ink-soft); text-transform: uppercase;
    font-size: 11.5px; letter-spacing: 2px; white-space: nowrap;
  }
  .divider {
    position: absolute; left: 310px; top: 60px; width: 2px; height: 240px;
    background: var(--ink-soft);
  }
  .contact {
    position: absolute; left: 334px; top: 122px;
    font-family: "Oswald", sans-serif; color: var(--ink-light);
  }
  .contact-name { font-size: 24px; font-weight: 500; letter-spacing: 2px; margin-bottom: 10px; }
  .contact-line {
    display: flex; align-items: center; gap: 8px;
    font-size: 17px; letter-spacing: 1.4px; line-height: 1.7; white-space: nowrap;
  }
  .contact-line svg { width: 15px; height: 15px; fill: var(--ink-soft); flex: none; }
</style>
</head>
<body>
<main class="stage">
  <section class="card card-back">
    <div class="wood" role="img" aria-label="Warm wood plank texture background"></div>
    <p class="back-brand">Cedarline<br>Joinery</p>
    <p class="back-url">www.cedarlinejoinery.com</p>
  </section>

  <section class="card card-front">
    <div class="front-brand">
      <p class="brand-name">Cedarline<br>Joinery</p>
      <p class="tagline">Handmade in Ashford, VT</p>
    </div>
    <div class="divider"></div>
    <div class="contact">
      <p class="contact-name">Marlo Finch</p>
      <p class="contact-line">
        <svg viewBox="0 0 16 16" aria-hidden="true"><path d="M2 5c0-2 2-3 6-3s6 1 6 3v1h-3V5H5v1H2zM4 7h8l2 7H2zm4 2a2 2 0 100 4 2 2 0 000-4z"/></svg>
        (555)417-6382
      </p>
      <p class="contact-line">
        <svg viewBox="0 0 16 16" aria-hidden="true"><path d="M1 3h14v10H1zm1.5 1.2V12h11V4.2L8 8.5z"/></svg>
        marlo@cedarlinejoinery.com
      </p>
    </div>
  </section>
</main>
</body>
</html>
```